Copper and Slate Mist NZ new website!

We are a new online vaping retailer and are looking for an awesome sleek website. We are going to be selling a variety of vaping products and gear. Our logo has just been developed and we would like to keep the website in line with the black, tan a white theme. We would like to trying watermarking or imposing the rottie into the background of the website on the home page, with the page being black and you can see the tan and white colours only.

Coding

Coded - Design and coding required

Number of Pages Required

2 page

Font styles to use
Serif
Sans Serif
Decorative

Requirements
Must have
• A home page and a standard page for products
• Stay in line with the colours in the logo

```html
<!DOCTYPE html>
<html lang="en">
<head>
<meta charset="utf-8">
<title>Copper and Slate Mist NZ</title>
<link href="https://fonts.googleapis.com/css2?family=Graduate&family=Lato:wght@400;700&family=Alegreya+Sans+SC:wght@700&display=swap" rel="stylesheet">
<style>
:root{
  --tan:#a45f17;
  --tan-light:#c77d2e;
  --black:#000;
  --charcoal:#1c1c1c;
  --panel:#2b2b2b;
  --white:#fff;
  --muted:#cfcfcf;
  --ink:#222;
}
*{box-sizing:border-box;margin:0;padding:0}
html,body{width:1200px;height:3673px;overflow:hidden;background:var(--black)}
body{position:relative;font-family:"Lato",sans-serif;color:var(--white)}
.abs{position:absolute}
.heading{font-family:"Graduate",serif;letter-spacing:1px}
.btn{position:absolute;background:var(--tan);color:var(--white);font-size:13px;text-transform:uppercase;display:flex;align-items:center;justify-content:center;letter-spacing:.5px}
.center{left:0;width:1200px;text-align:center}

/* header */
.hero{left:0;top:0;width:1200px;height:747px;background:radial-gradient(ellipse at 30% 50%,#3a3a3a 0%,#1a1a1a 60%,#0d0d0d 100%)}
.hero-photo{left:600px;top:0;width:600px;height:747px;background:linear-gradient(200deg,#8a8a8a 0%,#3c3c3c 35%,#141414 75%)}
.topline{left:81px;top:8px;font-size:14px;display:flex;align-items:center;gap:8px}
.nav{left:0;top:36px;width:1200px;height:52px;background:rgba(0,0,0,.75);border-bottom:2px solid var(--tan)}
.nav a{position:absolute;top:0;height:50px;display:flex;align-items:center;justify-content:center;color:var(--white);text-decoration:none;font-family:"Alegreya Sans SC",sans-serif;font-size:16px}
.nav a.active{background:var(--tan)}
.brand{left:548px;top:22px;display:flex;align-items:center;gap:8px;width:110px}
.brand .dot{width:30px;height:30px;border-radius:50%;background:var(--tan);flex:none}
.brand span{font-size:12px;font-weight:700;line-height:14px;color:var(--white)}
.icons{top:8px;left:1010px;display:flex;gap:22px}
.hero-kicker{left:81px;top:308px;font-size:14px}
.hero-title{left:81px;top:330px;font-size:58px;line-height:58px}
.dots{display:flex;gap:10px;justify-content:center}
.dots i{width:6px;height:6px;border-radius:50%;background:#888;display:block}
.dots i:first-child{background:var(--tan)}

/* promos */
.promo{top:752px;height:301px;background:var(--panel)}
.promo-img{position:absolute;background:linear-gradient(135deg,#7a2b1e,#3a1a12);border-radius:8px}
.promo h3{position:absolute;font-family:"Graduate",serif;font-size:34px;line-height:40px}
.promo p{position:absolute;font-size:12px}

/* trending */
.section-title{font-size:32px}
.tabs{top:1157px;left:0;width:1200px;display:flex;justify-content:center;gap:26px;font-size:12px}
.tabs span{padding:5px 8px}
.tabs span.on{background:var(--tan)}
.card{top:1220px;width:245px;height:367px;background:var(--white)}
.card .ph{position:absolute;left:45px;top:40px;width:155px;height:287px;background:linear-gradient(180deg,#d9d9d9,#7d7d7d)}
.pname{top:1608px;width:245px;text-align:center;font-size:14px}
.price{top:1650px;width:245px;text-align:center;font-size:22px}
.arrow{width:40px;height:40px;border-radius:50%;display:flex;align-items:center;justify-content:center;top:1378px}

/* testimonials */
.testi{left:0;top:1807px;width:1200px;height:417px;background:linear-gradient(90deg,#0e0e0e 0%,#262626 45%,#3a3a3a 70%,#161616 100%)}
.avatar{left:555px;top:1917px;width:90px;height:90px;border-radius:50%;border:4px solid var(--tan);background:linear-gradient(160deg,#b89a7e,#6a5444)}
.quote{left:240px;top:2020px;width:720px;text-align:center;font-size:13px;line-height:19px}

/* blogs */
.blog{top:2346px;width:338px;height:429px;background:var(--white);color:var(--ink)}
.blog .ph{position:absolute;left:8px;top:8px;width:322px;height:230px;background:linear-gradient(150deg,#9b9b9b,#2b2b2b)}
.blog h4{position:absolute;left:10px;top:252px;font-family:"Graduate",serif;font-size:14px}
.blog .meta{position:absolute;left:10px;top:276px;font-size:12px;color:#555;display:flex;gap:30px}
.blog p{position:absolute;left:10px;top:298px;width:315px;font-size:12px;line-height:16px;color:#444}
.blog .btn{left:10px;top:362px;width:155px;height:44px}

/* newsletter */
.news{left:0;top:2919px;width:1200px;height:375px;background:linear-gradient(90deg,#1a140f,#3b2d22 45%,#2a2018 70%,#524030)}
.news-input{left:309px;top:3105px;width:416px;height:47px;background:var(--white);color:#777;font-size:13px;font-style:italic;padding:16px 14px}

/* footer */
.footer{left:0;top:3294px;width:1200px;height:379px;background:var(--charcoal)}
.fhead{top:3390px;font-family:"Graduate",serif;font-size:15px}
.flist{top:3448px;font-size:12px;line-height:15px;list-style:none}
.flist li::before{content:"•";color:var(--tan);margin-right:9px}
.social{left:81px;top:3523px;display:flex;gap:8px}
.social i{width:22px;height:22px;border-radius:50%;background:var(--tan);display:block}
.pay{top:3603px;width:36px;height:22px;border-radius:3px}
</style>
</head>
<body>

<!-- hero -->
<section class="abs hero"></section>
<div class="abs hero-photo" role="img" aria-label="Vape tank device releasing thick white vapor clouds"></div>
<div class="abs topline">
  <svg width="16" height="16" viewBox="0 0 16 16"><circle cx="8" cy="8" r="7.3" fill="none" stroke="#fff" stroke-width="1.2"/><path d="M5.4 4.2l1.3 1.6-.8 1c.6 1.2 1.4 2 2.5 2.6l1-.8 1.6 1.3-.8 1.4c-2.8-.4-5.3-2.8-5.8-5.8z" fill="#fff"/></svg>
  (+064) 555 019 2
</div>
<div class="abs icons">
  <svg width="16" height="16" viewBox="0 0 16 16"><circle cx="8" cy="5" r="3.2" fill="none" stroke="#fff" stroke-width="1.5"/><path d="M2 15c0-3.5 2.7-5.5 6-5.5s6 2 6 5.5" fill="none" stroke="#fff" stroke-width="1.5"/></svg>
  <svg width="16" height="16" viewBox="0 0 16 16"><circle cx="10" cy="6" r="4.3" fill="none" stroke="#fff" stroke-width="1.6"/><path d="M7 9L1.5 14.5" stroke="#fff" stroke-width="2"/></svg>
  <svg width="16" height="18" viewBox="0 0 16 18"><rect x="2" y="5" width="12" height="12" fill="none" stroke="#fff" stroke-width="1.5"/><path d="M5 5V3.5a3 3 0 016 0V5" fill="none" stroke="#fff" stroke-width="1.5"/><circle cx="13" cy="14" r="3" fill="var(--tan)"/></svg>
</div>
<nav class="abs nav">
  <a class="active" style="left:211px;width:78px">Home</a>
  <a style="left:308px;width:84px">About us</a>
  <a style="left:421px;width:64px">Vapors</a>
  <a style="left:693px;width:103px">Accessories</a>
  <a style="left:828px;width:44px">Blog</a>
  <a style="left:906px;width:98px">Contact us</a>
</nav>
<div class="abs brand"><span class="dot"></span><span>Copper and Slate Mist NZ</span></div>

<div class="abs hero-kicker">Perfect Products That Fit You Need</div>
<h1 class="abs heading hero-title">BEST VAPING<br>FOR SMOKERS</h1>
<div class="btn" style="left:81px;top:465px;width:154px;height:45px">Shop now</div>
<div class="abs dots center" style="top:705px"><i></i><i></i><i></i></div>

<!-- promos -->
<section class="abs promo" style="left:0;width:595px">
  <div class="promo-img" role="img" aria-label="Red wooden pipe-style vape device" style="left:60px;top:50px;width:210px;height:200px"></div>
  <h3 style="left:338px;top:68px">NEW<br>ARRIVAL</h3>
  <p style="left:340px;top:150px">Lorem Ipsum is simply dummy text .</p>
  <div class="btn" style="left:340px;top:180px;width:154px;height:45px">Shop now</div>
</section>
<section class="abs promo" style="left:605px;width:595px">
  <div class="promo-img" role="img" aria-label="Red and black box mod vape kit with tank" style="left:60px;top:0;width:150px;height:290px;background:linear-gradient(180deg,#6a6a6a,#8e1d1d 55%,#1a1a1a)"></div>
  <h3 style="left:255px;top:68px">DISCOUNT<br>OFFER</h3>
  <p style="left:258px;top:150px">Get 30%off Discount on your 1st order</p>
  <div class="btn" style="left:258px;top:180px;width:154px;height:45px">Shop now</div>
</section>

<!-- trending -->
<h2 class="abs heading section-title center" style="top:1098px">TRENDING PRODUCTS</h2>
<div class="abs tabs"><span class="on">ALL</span><span>New Arrival</span><span>Best Seller</span><span>Discounted</span></div>

<div class="abs card" style="left:78px"><div class="ph" role="img" aria-label="E-liquid nic salt bottle"></div></div>
<div class="abs card" style="left:343px"><div class="ph" role="img" aria-label="USB vape battery charger cable"></div></div>
<div class="abs card" style="left:607px"><div class="ph" role="img" aria-label="Silver replacement tank with window"></div></div>
<div class="abs card" style="left:872px"><div class="ph" role="img" aria-label="Silver box mod starter kit"></div></div>

<div class="abs pname" style="left:78px">Daylong Vapor Nic Salt</div>
<div class="abs pname" style="left:343px">Vapor / e Cigratte Charger</div>
<div class="abs pname" style="left:607px;top:1600px;line-height:17px">Nimbus Mini Replacement Tank with<br>"T" Window</div>
<div class="abs pname" style="left:872px">Orbit 5S Kit</div>
<div class="abs price" style="left:78px">$13.99</div>
<div class="abs price" style="left:343px">$13.99</div>
<div class="abs price" style="left:607px">$13.99</div>
<div class="abs price" style="left:872px">$13.99</div>

<div class="abs arrow" style="left:56px;background:#333"><svg width="12" height="14" viewBox="0 0 12 14"><path d="M9 1L3 7l6 6" fill="none" stroke="#fff" stroke-width="2"/></svg></div>
<div class="abs arrow" style="left:1102px;background:var(--tan)"><svg width="12" height="14" viewBox="0 0 12 14"><path d="M3 1l6 6-6 6" fill="none" stroke="#fff" stroke-width="2"/></svg></div>
<div class="btn" style="left:522px;top:1710px;width:151px;height:43px">View more</div>

<!-- testimonials -->
<section class="abs testi" role="img" aria-label="Dark smoky background with a man exhaling vapor"></section>
<h2 class="abs heading section-title center" style="top:1855px">TESTIMONIALS</h2>
<div class="abs avatar" role="img" aria-label="Customer portrait"></div>
<div class="abs heading" style="left:236px;top:2002px;font-size:44px">“</div>
<p class="abs quote">Lorem Ipsum is simply dummy text of the printing and typesetting industry. Lorem Ipsum has been the industry's standard dummy text ever since the 1500s.</p>
<div class="abs heading" style="left:692px;top:2024px;font-size:44px">”</div>
<div class="abs heading center" style="top:2070px;font-size:14px">MARCUS</div>
<div class="abs center" style="top:2094px;font-size:12px;color:#e0a020;letter-spacing:2px">★★★★★</div>
<div class="abs dots center" style="top:2160px"><i></i><i></i><i></i></div>

<!-- blogs -->
<h2 class="abs heading section-title center" style="top:2270px">LATEST BLOGS</h2>
<article class="abs blog" style="left:78px">
  <div class="ph" role="img" aria-label="Person exhaling vapor from a mod"></div>
  <h4>BLOG POST#01</h4>
  <div class="meta"><span>▦ 9.May.2019</span><span>◌ Comments (12)</span></div>
  <p>Lorem Ipsum is simply dummy text of the printing and typesetting industry. Lorem Ipsum has been the industry's standard dummy text ever since the 1500s.</p>
  <div class="btn">Read more</div>
</article>
<article class="abs blog" style="left:429px">
  <div class="ph" role="img" aria-label="Woman in a cap vaping in a shop" style="background:linear-gradient(150deg,#c9b7a4,#5b4433)"></div>
  <h4>BLOG POST#02</h4>
  <div class="meta"><span>▦ 9.May.2019</span><span>◌ Comments (12)</span></div>
  <p>Lorem Ipsum is simply dummy text of the printing and typesetting industry. Lorem Ipsum has been the industry's standard dummy text ever since the 1500s.</p>
  <div class="btn">Read more</div>
</article>
<article class="abs blog" style="left:779px">
  <div class="ph" role="img" aria-label="Black vape mod with smoke on dark background" style="background:linear-gradient(150deg,#5a5a5a,#0a0a0a)"></div>
  <h4>BLOG POST#03</h4>
  <div class="meta"><span>▦ 9.May.2019</span><span>◌ Comments (12)</span></div>
  <p>Lorem Ipsum is simply dummy text of the printing and typesetting industry. Lorem Ipsum has been the industry's standard dummy text ever since the 1500s.</p>
  <div class="btn">Read more</div>
</article>
<div class="btn" style="left:522px;top:2829px;width:151px;height:43px">View more</div>

<!-- newsletter -->
<section class="abs news" role="img" aria-label="Black and tan dog resting indoors, darkened"></section>
<h2 class="abs heading section-title center" style="top:3014px">JOIN US FOR NEWSLETTER</h2>
<div class="abs news-input">Email Address</div>
<div class="btn" style="left:730px;top:3105px;width:154px;height:47px">Subscribe</div>

<!-- footer -->
<footer class="abs footer"></footer>
<div class="abs" style="left:81px;top:3325px;display:flex;align-items:center;gap:10px">
  <span style="width:44px;height:44px;border-radius:50%;background:var(--tan);display:block"></span>
  <span style="font-size:14px;font-weight:700">Copper and Slate Mist NZ</span>
</div>
<p class="abs" style="left:81px;top:3452px;width:250px;font-size:12px;line-height:15px">Lorem Ipsum is simply dummy text of the printing and typesetting industry.</p>
<div class="abs" style="left:81px;top:3488px;font-size:12px;color:var(--tan);text-decoration:underline">READ MORE</div>
<div class="abs social"><i></i><i></i><i></i><i></i><i></i></div>

<div class="abs fhead" style="left:385px">QUICK LINKS</div>
<ul class="abs flist" style="left:390px;top:3446px"><li>Home</li><li>About us</li><li>Vapors</li><li>Accessories</li><li>Blog</li><li>Contact us</li></ul>
<div class="abs fhead" style="left:568px">ACCOUNT</div>
<ul class="abs flist" style="left:573px;top:3446px"><li>Login</li><li>Register</li><li>My Profile</li><li>My Cart</li><li>Checkout</li></ul>
<div class="abs fhead" style="left:735px">INFORMATION</div>
<ul class="abs flist" style="left:740px;top:3446px"><li>Return Policy</li><li>Privacy policy</li><li>Terms &amp; conditions</li></ul>
<div class="abs fhead" style="left:933px">CONTACT DETAIL</div>
<ul class="abs" style="left:936px;top:3446px;list-style:none;font-size:12px;line-height:15px">
  <li><span style="color:var(--tan)">☏</span>&nbsp; (+064) 555 019 2</li>
  <li><span style="color:var(--tan)">☏</span>&nbsp; (+064) 555 019 2</li>
  <li><span style="color:var(--tan)">✉</span>&nbsp; info@copperslatemist.co.nz</li>
  <li><span style="color:var(--tan)">⌖</span>&nbsp; 14 Harbour Lane,<br>&nbsp;&nbsp;&nbsp;&nbsp;&nbsp;Wellington 6011</li>
</ul>

<div class="abs" style="left:81px;top:3576px;width:1036px;height:1px;background:#555"></div>
<div class="abs" style="left:81px;top:3608px;font-size:12px">Copyright © 2019 copperslatemist.co.nz. All Rights Reserved.</div>
<div class="abs pay" style="left:940px;background:#e8e8e8"></div>
<div class="abs pay" style="left:983px;background:#1c3f94"></div>
<div class="abs pay" style="left:1026px;background:#d9d9d9"></div>
<div class="abs pay" style="left:1069px;background:#2a7bc0"></div>

</body>
</html>
```